Property Auctions with Gareth Pemberley

Podcast cover art 3000px by 3000px. Eye catching for a weekly podcast. The words should read Property Auctions (large font) with Gareth Pemberley (smaller font)

I would like the font and colours to be similar to my book, a copy of which I have attached.

New and experienced property investors looking to purchase at a property auction

```html
<!DOCTYPE html>
<html lang="en">
<head>
<meta charset="utf-8">
<title>Property Auctions with Gareth Pemberley</title>
<link rel="stylesheet" href="https://fonts.googleapis.com/css2?family=Oswald:wght@700&family=Great+Vibes&display=swap">
<style>
  :root {
    --ink: #0b0b0b;
    --smoke: #2a2a2a;
    --gold-deep: #9c6d1f;
    --gold-mid: #c9a23f;
    --gold-light: #f0e28e;
    --white: #ffffff;
  }
  html, body {
    margin: 0;
    padding: 0;
    width: 1191px;
    height: 1200px;
    overflow: hidden;
    background: var(--ink);
  }
  .cover {
    display: block;
    width: 1191px;
    height: 1200px;
  }
  .title {
    font-family: "Oswald", "Arial Narrow", sans-serif;
    font-weight: 700;
  }
  .connector {
    font-family: "Great Vibes", cursive;
    fill: var(--white);
  }
</style>
</head>
<body>
<svg class="cover" viewBox="0 0 1191 1200" xmlns="http://www.w3.org/2000/svg">
  <defs>
    <linearGradient id="gold-foil" x1="0" y1="0" x2="1" y2="0">
      <stop offset="0" stop-color="var(--gold-deep)"/>
      <stop offset="0.12" stop-color="var(--gold-mid)"/>
      <stop offset="0.22" stop-color="var(--gold-light)"/>
      <stop offset="0.32" stop-color="var(--gold-mid)"/>
      <stop offset="0.45" stop-color="var(--gold-deep)"/>
      <stop offset="0.58" stop-color="var(--gold-light)"/>
      <stop offset="0.7" stop-color="var(--gold-mid)"/>
      <stop offset="0.85" stop-color="var(--gold-light)"/>
      <stop offset="1" stop-color="var(--gold-deep)"/>
    </linearGradient>
    <radialGradient id="backdrop-glow" cx="0.7" cy="0.8" r="0.7">
      <stop offset="0" stop-color="#4a4a4a"/>
      <stop offset="0.6" stop-color="var(--smoke)"/>
      <stop offset="1" stop-color="var(--ink)"/>
    </radialGradient>
    <radialGradient id="emblem-glow" cx="0.5" cy="0.55" r="0.55">
      <stop offset="0" stop-color="var(--gold-mid)" stop-opacity="0.55"/>
      <stop offset="0.6" stop-color="var(--gold-deep)" stop-opacity="0.3"/>
      <stop offset="1" stop-color="var(--gold-deep)" stop-opacity="0"/>
    </radialGradient>
    <radialGradient id="flare" cx="0.5" cy="0.5" r="0.5">
      <stop offset="0" stop-color="#fffbe6" stop-opacity="0.95"/>
      <stop offset="0.4" stop-color="#f3dc86" stop-opacity="0.5"/>
      <stop offset="1" stop-color="#f3dc86" stop-opacity="0"/>
    </radialGradient>
  </defs>

  <rect class="backdrop" x="0" y="0" width="1191" height="1200" fill="var(--ink)"/>
  <rect class="backdrop-photo" x="0" y="0" width="1191" height="1200" fill="url(#backdrop-glow)" opacity="0.75"
        role="img" aria-label="Faded black and white photo of a model house on banknotes beside an auction gavel"/>

  <g class="headline title" fill="url(#gold-foil)">
    <text x="107" y="315" font-size="228" textLength="976" lengthAdjust="spacingAndGlyphs">PROPERTY</text>
    <text x="123" y="530" font-size="228" textLength="934" lengthAdjust="spacingAndGlyphs">AUCTIONS</text>
  </g>
  <circle class="flare" cx="520" cy="215" r="45" fill="url(#flare)"/>

  <text class="connector" x="145" y="628" font-size="170">with</text>

  <g class="host-name title" fill="url(#gold-foil)">
    <text x="113" y="864" font-size="157" textLength="462" lengthAdjust="spacingAndGlyphs">GARETH</text>
    <text x="107" y="1020" font-size="157" textLength="476" lengthAdjust="spacingAndGlyphs">PEMBERLEY</text>
  </g>

  <rect class="emblem-area" x="635" y="627" width="540" height="450" rx="24" fill="url(#emblem-glow)"
        role="img" aria-label="Gold house outline with lit windows and a 3D gold pound sign"/>
</svg>
</body>
</html>
```